Design Challege - Simplify a Complex Message

We have a new website design, but one of the pages presents a particular problem.

Our company does ERP implementations. We have developed a proprietary approach to these implementations based on the idea that you must get eight (and only eight) things right. These eight things are listed below, summarized in one or two words each:

1. Value
2. Capability
3. Functionality
4. Data
5. Technology
6. Change Leadership
7. Quality
8. Governance

Each of these eight things can be summarized in a short paragraph, but when you combine all eight summaries with a brief introductory text, the result is a lot of text - so much text that the casual surfer may be overwhelmed by it.

The winning design will find an engaging way to present the information in a way that presents a high-level summary, using icons and one- or two-word descriptions above but revealing more information when clicked.

Our current design for this information, with a paragraph describing the eight elements in a table, is included as an upload in PDF and Microsoft Word formats. We are looking for a creative way to display these eight things, showing the detail only when the user wants to see it.

The website is being built in WordPress, using Elementor as a page builder.

We will implement (code) the page, but the winner will be asked to specify the widget or other add-in if one is required.

The design does not need to include a header or footer, we have those.

Target Market(s)

Business executives working in technology

Industry/Entity Type

Any

Number of Pages Required

1 page

Font styles to use
Sans Serif

Requirements
Must have
• A design for the body of the page, but not the header or footer.
Nice to have
• Unique icons or images appropriate for each of the eight things.
Should not have
• A lot of text on one page

```html
<!DOCTYPE html>
<html lang="en">
<head>
<meta charset="utf-8">
<title>ERP Implementations – Eight Things to Get Right</title>
<link rel="stylesheet" href="https://fonts.googleapis.com/css2?family=Montserrat:wght@400;600;700;800&display=swap">
<style>
  :root {
    --bg: #181818;
    --card: #1f1f1f;
    --accent: #2a8fd8;
    --heading: #ffffff;
    --body: #d6d6d6;
    --muted: #c4c4c4;
    --label: #bdbdbd;
  }
  * { box-sizing: border-box; margin: 0; padding: 0; }
  html, body { width: 1200px; height: 1147px; overflow: hidden; background: var(--bg); }
  body { position: relative; font-family: "Montserrat", Arial, sans-serif; color: var(--body); }

  .page-title {
    position: absolute; left: 231px; top: 64px;
    font-size: 20px; font-weight: 600; letter-spacing: 0.4px; color: var(--accent);
    padding-bottom: 2px; border-bottom: 1.5px solid var(--accent);
  }
  .page-subtitle { position: absolute; left: 231px; top: 107px; font-size: 13px; font-weight: 700; color: var(--heading); }
  .intro { position: absolute; left: 231px; width: 420px; font-size: 9.3px; line-height: 14px; color: var(--body); }
  .intro-1 { top: 135px; }
  .intro-2 { top: 176px; }

  .view-label {
    position: absolute; left: 18px; font-size: 12.5px; font-weight: 700;
    font-variant: small-caps; letter-spacing: 0.3px; color: var(--label);
  }

  .card {
    position: absolute; width: 175px; height: 162px;
    background: var(--card); border-radius: 9px;
    box-shadow: 0 4px 10px rgba(0,0,0,0.35);
    text-align: center;
  }
  .card.is-open { height: 347px; }
  .card-icon { position: absolute; left: 50%; top: 25px; width: 40px; height: 40px; margin-left: -20px; }
  .card-icon svg { width: 40px; height: 40px; fill: none; stroke: var(--accent); stroke-width: 1.4; stroke-linecap: round; stroke-linejoin: round; }
  .card-title { position: absolute; left: 0; right: 0; top: 82px; font-size: 10px; font-weight: 800; color: var(--heading); letter-spacing: 0.2px; }
  .card-text { position: absolute; left: 12px; right: 12px; top: 103px; font-size: 9px; line-height: 15px; color: var(--muted); }
  .card.is-open .card-text { top: 108px; left: 20px; right: 16px; font-size: 8.8px; }
  .card-toggle { position: absolute; left: 50%; bottom: 13px; margin-left: -5px; width: 10px; height: 6px; }
  .card-toggle svg { width: 10px; height: 6px; fill: var(--accent); display: block; }
  .card.is-open .card-toggle { bottom: 14px; }
</style>
</head>
<body>
<svg width="0" height="0" style="position:absolute">
  <defs>
    <symbol id="icon-value" viewBox="0 0 40 40">
      <circle cx="20" cy="24" r="6.5"/><circle cx="20" cy="24" r="4.5"/>
      <path d="M21.3 21.6c-.6-.5-2.6-.6-2.6.7s2.7 1 2.7 2.4-2 1.2-2.8.6M20 20.5v7"/>
      <path d="M20 16V6M17 9l3-3 3 3M9 29v-9M6.5 22.5 9 20l2.5 2.5M31 29v-9M28.5 22.5 31 20l2.5 2.5M13 28v-2M27 28v-2"/>
    </symbol>
    <symbol id="icon-capability" viewBox="0 0 40 40">
      <circle cx="20" cy="19" r="3"/><path d="M14 34v-6a6 6 0 0 1 12 0v6M18 34v-5h4v5"/>
      <path d="M20 7a2.5 2.5 0 0 1 1.5 4.5v1h-3v-1A2.5 2.5 0 0 1 20 7zM20 4v1M16 6l.7.7M24 6l-.7.7"/>
      <circle cx="30" cy="12" r="2.5" stroke-dasharray="1.5 1"/><circle cx="30" cy="12" r="1"/>
      <path d="M8 14l2 2 3-3M9 24v5M7 26l2-2 2 2M31 22l1 2 2 .3-1.5 1.4.4 2-1.9-1-1.9 1 .4-2L28 24.3l2-.3z"/>
    </symbol>
    <symbol id="icon-functionality" viewBox="0 0 40 40">
      <circle cx="24" cy="11" r="5.5" stroke-width="3" stroke-dasharray="2 1.6"/><circle cx="24" cy="11" r="2.2"/>
      <circle cx="12" cy="25" r="5.5" stroke-width="3" stroke-dasharray="2 1.6"/><circle cx="12" cy="25" r="2.2"/>
      <circle cx="29" cy="29" r="5.5" stroke-width="3" stroke-dasharray="2 1.6"/><circle cx="29" cy="29" r="2.2"/>
    </symbol>
    <symbol id="icon-data" viewBox="0 0 40 40">
      <path d="M11 26a6 6 0 0 1-.5-12A9 9 0 0 1 28 12.5a6.8 6.8 0 0 1 2 13.5"/>
      <path d="M20 16v16M15 19v9M25 19v9"/><circle cx="20" cy="33.5" r="1.5"/><circle cx="15" cy="29.5" r="1.5"/><circle cx="25" cy="29.5" r="1.5"/>
    </symbol>
    <symbol id="icon-technology" viewBox="0 0 40 40">
      <rect x="6" y="6" width="28" height="28"/><path d="M9 9h5M9 9v5M31 31h-5M31 31v-5"/>
      <circle cx="14" cy="14" r="2.5"/><circle cx="25" cy="15" r="2.5"/><circle cx="14" cy="25" r="2.5"/><circle cx="24" cy="24" r="3"/>
      <path d="M16.5 14h6M14 16.5v6M23 17l-7 7M26 26l5 5"/>
    </symbol>
    <symbol id="icon-change" viewBox="0 0 40 40">
      <circle cx="20" cy="16" r="3"/><path d="M14 26a6 6 0 0 1 12 0"/>
      <circle cx="9" cy="21" r="2.5"/><path d="M4 30a5 5 0 0 1 10 0M26 30a5 5 0 0 1 10 0"/><circle cx="31" cy="21" r="2.5"/>
      <path d="M20 7v2M13 10l1.3 1.3M27 10l-1.3 1.3M11 16h1M28 16h1"/>
    </symbol>
    <symbol id="icon-quality" viewBox="0 0 40 40">
      <path d="M20 5l3 2 3.6-.2 1 3.5 3 2-1.2 3.4 1.2 3.4-3 2-1 3.5-3.6-.2-3 2-3-2-3.6.2-1-3.5-3-2 1.2-3.4-1.2-3.4 3-2 1-3.5 3.6.2z"/>
      <path d="M15.5 16l3 3 6-6M14 25l-3 9 3.5-1.5 2 3 2.5-7M26 25l3 9-3.5-1.5-2 3-2.5-7"/>
    </symbol>
    <symbol id="icon-governance" viewBox="0 0 40 40">
      <circle cx="20" cy="8" r="2.5"/><path d="M16 15a4 4 0 0 1 8 0z"/>
      <path d="M20 15v3M9 18h22M9 18v3M31 18v3M20 18v3"/>
      <circle cx="9" cy="25" r="2.3"/><circle cx="20" cy="25" r="2.3"/><circle cx="31" cy="25" r="2.3"/>
      <path d="M5 33a4 4 0 0 1 8 0zM16 33a4 4 0 0 1 8 0zM27 33a4 4 0 0 1 8 0z"/>
      <path d="M13 11h-2v3M27 11h2v3"/>
    </symbol>
    <symbol id="arrow-down" viewBox="0 0 10 6"><path d="M0 0h10L5 6z"/></symbol>
    <symbol id="arrow-up" viewBox="0 0 10 6"><path d="M0 6h10L5 0z"/></symbol>
  </defs>
</svg>

<h1 class="page-title">ERP IMPLEMENTATIONS</h1>
<h2 class="page-subtitle">Eight Things to Get Right</h2>
<p class="intro intro-1">Like the roots and branches of a tree, there are many considerations in an ERP implementation. Focus too much on the minor details, and you can lose sight of the tree.</p>
<p class="intro intro-2">In an ERP implementation, you must get eight major things right to be successful. Ignore any of them, and your implementation will fail. Get them right, and you will likely succeed.</p>

<div class="view-label" style="top:389px">(Normal View)</div>
<div class="view-label" style="top:848px">(Clicked View)</div>

<!-- Normal view -->
<section class="card" style="left:231px;top:230px"><div class="card-icon"><svg><use href="#icon-value"/></svg></div><h3 class="card-title">VALUE</h3><p class="card-text">High-value, aligned, and<br>resource-efficient project</p><span class="card-toggle"><svg><use href="#arrow-down"/></svg></span></section>
<section class="card" style="left:419px;top:230px"><div class="card-icon"><svg><use href="#icon-capability"/></svg></div><h3 class="card-title">CAPABILITY</h3><p class="card-text">A capable team implementing<br>the project on their own</p><span class="card-toggle"><svg><use href="#arrow-down"/></svg></span></section>
<section class="card" style="left:606px;top:230px"><div class="card-icon"><svg><use href="#icon-functionality"/></svg></div><h3 class="card-title">FUNCTIONALITY</h3><p class="card-text">ERP supports current<br>and future projects</p><span class="card-toggle"><svg><use href="#arrow-down"/></svg></span></section>
<section class="card" style="left:794px;top:230px"><div class="card-icon"><svg><use href="#icon-data"/></svg></div><h3 class="card-title">DATA</h3><p class="card-text">Insights require careful<br>data management</p><span class="card-toggle"><svg><use href="#arrow-down"/></svg></span></section>

<section class="card" style="left:231px;top:414px"><div class="card-icon"><svg><use href="#icon-technology"/></svg></div><h3 class="card-title">TECHNOLOGY</h3><p class="card-text">Consider integration and<br>scalability of your system</p><span class="card-toggle"><svg><use href="#arrow-down"/></svg></span></section>
<section class="card" style="left:419px;top:414px"><div class="card-icon"><svg><use href="#icon-change"/></svg></div><h3 class="card-title">CHANGE LEADERSHIP</h3><p class="card-text">Focus on human aspects in ERP<br>implementation for success</p><span class="card-toggle"><svg><use href="#arrow-down"/></svg></span></section>
<section class="card" style="left:606px;top:414px"><div class="card-icon"><svg><use href="#icon-quality"/></svg></div><h3 class="card-title">QUALITY</h3><p class="card-text">Take an approach to quality<br>beginning with perceptions</p><span class="card-toggle"><svg><use href="#arrow-down"/></svg></span></section>
<section class="card" style="left:794px;top:414px"><div class="card-icon"><svg><use href="#icon-governance"/></svg></div><h3 class="card-title">GOVERNANCE</h3><p class="card-text">Without both mangement &amp;<br>leadership, the best projects fail</p><span class="card-toggle"><svg><use href="#arrow-down"/></svg></span></section>

<!-- Clicked view -->
<section class="card is-open" style="left:231px;top:689px"><div class="card-icon"><svg><use href="#icon-value"/></svg></div><h3 class="card-title">VALUE</h3><p class="card-text">The project must provide value that significantly exceeds potential project costs and should be aligned with the company's strategy. Its value and strategic alignment must be part of a vision shared by the company's leadership. Value from the project must be delivered in a way that respects resource constraints.</p><span class="card-toggle"><svg><use href="#arrow-up"/></svg></span></section>
<section class="card" style="left:419px;top:689px"><div class="card-icon"><svg><use href="#icon-capability"/></svg></div><h3 class="card-title">CAPABILITY</h3><p class="card-text">A capable team implementing<br>the project on their own</p><span class="card-toggle"><svg><use href="#arrow-down"/></svg></span></section>
<section class="card" style="left:607px;top:689px"><div class="card-icon"><svg><use href="#icon-functionality"/></svg></div><h3 class="card-title">FUNCTIONALITY</h3><p class="card-text">ERP supports current<br>and future projects</p><span class="card-toggle"><svg><use href="#arrow-down"/></svg></span></section>
<section class="card" style="left:794px;top:689px"><div class="card-icon"><svg><use href="#icon-data"/></svg></div><h3 class="card-title">DATA</h3><p class="card-text">Insights require careful<br>data management</p><span class="card-toggle"><svg><use href="#arrow-down"/></svg></span></section>

<section class="card" style="left:419px;top:874px"><div class="card-icon"><svg><use href="#icon-change"/></svg></div><h3 class="card-title">CHANGE LEADERSHIP</h3><p class="card-text">Focus on human aspects in ERP<br>implementation for success</p><span class="card-toggle"><svg><use href="#arrow-down"/></svg></span></section>
<section class="card" style="left:607px;top:874px"><div class="card-icon"><svg><use href="#icon-quality"/></svg></div><h3 class="card-title">QUALITY</h3><p class="card-text">Take an approach to quality<br>beginning with perceptions</p><span class="card-toggle"><svg><use href="#arrow-down"/></svg></span></section>
<section class="card" style="left:794px;top:874px"><div class="card-icon"><svg><use href="#icon-governance"/></svg></div><h3 class="card-title">GOVERNANCE</h3><p class="card-text">Without both mangement &amp;<br>leadership, the best projects fail</p><span class="card-toggle"><svg><use href="#arrow-down"/></svg></span></section>
</body>
</html>
```